2 posters for martial arts gym

Need 2 separate different posters for my martial arts gym. 1 poster needs to be a manga or cartoon looking image with my logo (attached). the other poster needs to be a professional look with 3 stick men images, boxing, kickboxing, Jiu jitsu with my logo also. colors need to be black and red. prefer no copied images.
i have attached my logo (torvik mma) and some images i like to help.

```html
<!DOCTYPE html>
<html lang="en">
<head>
<meta charset="utf-8">
<title>Martial Arts Gym Poster</title>
<link rel="stylesheet" href="https://fonts.googleapis.com/css2?family=Alfa+Slab+One&family=Archivo+Black&family=Roboto:wght@700&display=swap">
<style>
  :root {
    --page: #e9e6e2;
    --poster: #2b2b30;
    --poster-deep: #1f1f23;
    --red: #e8323a;
    --red-glow: #ff5a5a;
    --white: #f6f6f6;
    --ink: #141414;
    --art-light: #d9d6cf;
    --art-mid: #8d8a84;
    --art-dark: #3c3b39;
    --figure-light: #e4e4e4;
    --figure-dark: #3a3a40;
  }
  * { box-sizing: border-box; margin: 0; padding: 0; }
  html, body {
    width: 1200px; height: 800px; overflow: hidden;
    background: var(--page);
  }
  .stage {
    width: 1200px; height: 800px;
    display: flex; align-items: center; justify-content: center;
  }
  .poster {
    position: relative;
    width: 500px; height: 710px;
    background: linear-gradient(160deg, var(--poster) 0%, var(--poster-deep) 100%);
    overflow: hidden;
    box-shadow: 0 6px 20px rgba(0,0,0,.18);
  }
  .hero-art {
    position: absolute;
    left: 90px; top: 40px;
    width: 320px; height: 320px;
    border-radius: 50%;
    background: linear-gradient(120deg, var(--art-light) 0%, var(--art-mid) 45%, var(--art-dark) 50%, var(--art-light) 52%, #f0efec 100%);
  }
  .chevrons {
    position: absolute;
    width: 34px; height: 28px;
  }
  .chevrons--top { left: 34px; top: 150px; }
  .chevrons--side { right: 40px; top: 380px; }
  .dash-line {
    position: absolute;
    height: 4px;
    background: repeating-linear-gradient(90deg, var(--red) 0 6px, transparent 6px 11px);
  }
  .dash-line--top { left: 62px; top: 110px; width: 62px; transform: rotate(-12deg); }
  .dash-line--title { left: 30px; top: 425px; width: 60px; transform: rotate(-12deg); }
  .dash-line--side { right: 20px; top: 200px; width: 40px; transform: rotate(80deg); }
  .headline {
    position: absolute;
    left: 0; right: 0; top: 405px;
    text-align: center;
    font-family: "Alfa Slab One", serif;
    font-size: 46px;
    line-height: 1.1;
    letter-spacing: 2px;
    color: #ffd9d9;
    text-shadow: 0 0 6px var(--red-glow), 0 0 14px var(--red), 0 0 22px var(--red);
    transform: rotate(-4deg);
  }
  .discipline-strip {
    position: absolute;
    left: 20px; top: 560px;
    width: 400px; height: 46px;
    transform: rotate(-7deg);
    transform-origin: left center;
    background: linear-gradient(90deg, var(--figure-dark) 0%, var(--figure-light) 18%, var(--figure-dark) 36%, var(--figure-light) 54%, var(--figure-dark) 72%, var(--figure-light) 90%, var(--figure-dark) 100%);
    opacity: .35;
    border-radius: 3px;
  }
  .brand-band {
    position: absolute;
    left: 0; bottom: 0;
    width: 500px; height: 130px;
  }
  .brand {
    position: absolute;
    right: 22px; bottom: 32px;
    display: flex; align-items: center; gap: 10px;
  }
  .brand__mark {
    width: 12px; height: 12px;
    background: var(--red);
  }
  .brand__name {
    font-family: "Archivo Black", sans-serif;
    font-size: 30px;
    line-height: 1;
    color: var(--ink);
    letter-spacing: 1px;
  }
  .brand__tagline {
    position: absolute;
    right: 24px; bottom: 12px;
    font-family: "Roboto", sans-serif;
    font-weight: 700;
    font-size: 11px;
    letter-spacing: 1px;
    color: var(--red);
  }
</style>
</head>
<body>
<main class="stage">
  <article class="poster">
    <div class="hero-art" role="img" aria-label="Illustration of an armoured samurai beside a boxer in red gloves, split diagonally inside a circle"></div>

    <svg class="chevrons chevrons--top" viewBox="0 0 34 28" aria-hidden="true">
      <polyline points="3,4 15,14 3,24" fill="none" stroke="var(--red)" stroke-width="3"/>
      <polyline points="16,4 28,14 16,24" fill="none" stroke="var(--red)" stroke-width="3"/>
    </svg>
    <svg class="chevrons chevrons--side" viewBox="0 0 34 28" aria-hidden="true">
      <polyline points="3,4 15,14 3,24" fill="none" stroke="var(--red)" stroke-width="3"/>
      <polyline points="16,4 28,14 16,24" fill="none" stroke="var(--red)" stroke-width="3"/>
    </svg>

    <span class="dash-line dash-line--top"></span>
    <span class="dash-line dash-line--title"></span>
    <span class="dash-line dash-line--side"></span>

    <h1 class="headline">MARTIAL<br>ARTS GYM</h1>

    <div class="discipline-strip" role="img" aria-label="Row of white stick figures performing boxing, kickboxing and jiu-jitsu moves"></div>

    <svg class="brand-band" viewBox="0 0 500 130" aria-hidden="true">
      <polygon points="60,130 100,60 500,10 500,130" fill="var(--white)"/>
    </svg>
    <div class="brand">
      <span class="brand__mark"></span>
      <span class="brand__name">TORVIK-MMA</span>
    </div>
    <p class="brand__tagline">BOXING / KICKBOXING / JIU-JITSU</p>
  </article>
</main>
</body>
</html>
```